Needing a business Card for new fire company.

Dalvo, sales fire equipment and parts. We also do tree clearing for the forest service. My logo will be attached to this. I am also looking for a design that when people see the card it stick with them and they will remember my sales team giving it to them.

```html
<!DOCTYPE html>
<html lang="en">
<head>
<meta charset="utf-8">
<title>Dalvo Business Card</title>
<link rel="stylesheet" href="https://fonts.googleapis.com/css2?family=Montserrat:wght@400;500;700;800&display=swap">
<style>
  :root {
    --stage: #e9e6e2;
    --card-dark: #060606;
    --card-light: #ffffff;
    --brand-red: #c8262d;
    --ink: #151515;
    --muted-line: #c4c4c4;
    --white: #ffffff;
  }
  * { box-sizing: border-box; margin: 0; padding: 0; }
  html, body {
    width: 1200px; height: 914px; overflow: hidden;
    background: var(--stage);
    font-family: "Montserrat", sans-serif;
  }
  .canvas {
    position: relative; width: 1200px; height: 914px;
    display: flex; flex-direction: column; align-items: center; justify-content: center; gap: 38px;
  }
  .card {
    position: relative; width: 700px; height: 400px;
    box-shadow: 0 10px 28px rgba(0,0,0,.18);
  }
  .card--front { background: var(--card-dark); display: flex; align-items: center; justify-content: center; }
  .card--back { background: var(--card-light); }

  .wordmark {
    display: flex; align-items: center; gap: 16px;
    font-weight: 800; letter-spacing: 4px; text-transform: uppercase;
  }
  .wordmark__dot { width: 22px; height: 22px; border-radius: 50%; background: var(--brand-red); }
  .card--front .wordmark { color: var(--white); font-size: 92px; }
  .card--back .wordmark {
    position: absolute; left: 70px; top: 110px;
    color: var(--ink); font-size: 66px; gap: 12px;
  }
  .card--back .wordmark__dot { width: 16px; height: 16px; }

  .person {
    position: absolute; left: 430px; top: 170px;
    padding-left: 26px;
  }
  .person::before {
    content: ""; position: absolute; left: 0; top: 4px;
    width: 2px; height: 48px; background: var(--brand-red);
  }
  .person__name { color: var(--brand-red); font-weight: 700; font-size: 30px; letter-spacing: 1.5px; }
  .person__title { color: var(--ink); font-weight: 400; font-size: 15px; letter-spacing: 1.5px; margin-top: 2px; }

  .contact-list {
    position: absolute; left: 400px; top: 250px;
    list-style: none; padding-left: 22px;
    border-left: 1px solid var(--muted-line);
  }
  .contact-list li {
    display: flex; align-items: center; gap: 12px;
    color: var(--ink); font-size: 15px; font-weight: 500; letter-spacing: 1.2px;
    height: 27px;
  }
  .contact-list svg { width: 15px; height: 15px; fill: var(--brand-red); flex: none; }
</style>
</head>
<body>
<main class="canvas">
  <section class="card card--front" aria-label="Card front">
    <div class="wordmark"><span class="wordmark__dot"></span>Dalvo</div>
  </section>

  <section class="card card--back" aria-label="Card back">
    <div class="wordmark"><span class="wordmark__dot"></span>Dalvo</div>

    <div class="person">
      <p class="person__name">Marcus Hale</p>
      <p class="person__title">General Manager</p>
    </div>

    <ul class="contact-list">
      <li>
        <svg viewBox="0 0 16 16" aria-hidden="true"><path d="M8 0a5.5 5.5 0 0 0-5.5 5.5C2.5 9.5 8 16 8 16s5.5-6.5 5.5-10.5A5.5 5.5 0 0 0 8 0zm0 8a2.5 2.5 0 1 1 0-5 2.5 2.5 0 0 1 0 5z"/></svg>
        Your Address Here
      </li>
      <li>
        <svg viewBox="0 0 16 16" aria-hidden="true"><path d="M3.6 1.2 5.8 3.6 4.6 5.6c.9 2.2 2.8 4.1 5 5l2-1.2 2.4 2.2-1.4 2.6C7.4 14.4 1.6 8.6 1 3.4z"/></svg>
        555 210-4387
      </li>
      <li>
        <svg viewBox="0 0 16 16" aria-hidden="true"><path d="M1 3h14v1.2L8 9 1 4.2zm0 2.6 7 4.8 7-4.8V13H1z"/></svg>
        info@dalvo.com
      </li>
      <li>
        <svg viewBox="0 0 16 16" aria-hidden="true"><path d="M8 0a8 8 0 1 0 0 16A8 8 0 0 0 8 0zm5.9 7h-2.6a12 12 0 0 0-1-4.8A6 6 0 0 1 13.9 7zM8 2c.8 1 1.4 2.8 1.5 5h-3C6.6 4.8 7.2 3 8 2zM5.7 2.2a12 12 0 0 0-1 4.8H2.1a6 6 0 0 1 3.6-4.8zM2.1 9h2.6c.1 1.8.4 3.4 1 4.8A6 6 0 0 1 2.1 9zM8 14c-.8-1-1.4-2.8-1.5-5h3c-.1 2.2-.7 4-1.5 5zm2.3-.2c.6-1.4.9-3 1-4.8h2.6a6 6 0 0 1-3.6 4.8z"/></svg>
        www.dalvo.com
      </li>
    </ul>
  </section>
</main>
</body>
</html>
```